Mobile friendly Website design

Client is a packaging equipment company that would like a clean, mobile friendly design. They want a different home page than what they have now. The home page should have the traditional sliders, content area, services are and a featured products area. Please provide an internal page design too.

Target Market(s)

Companies who use packaging equipment, shrink wrappers, heat sealers and carton erectors.

Industry/Entity Type

It Company

Number of Pages Required

2 page

Font styles to use
Serif
Sans Serif

Requirements
Must have
• Must have a clean, mobile friendly design.

```html
<!DOCTYPE html>
<html lang="en">
<head>
<meta charset="utf-8">
<title>Harlow Packaging</title>
<link href="https://fonts.googleapis.com/css2?family=Open+Sans:wght@300;400;600;700&family=Roboto+Slab:wght@700&display=swap" rel="stylesheet">
<style>
:root{
  --red:#c81f2d;
  --navy:#2a2560;
  --navy-dark:#211c4f;
  --ink:#333;
  --muted:#777;
  --line:#e2e2e2;
  --footer:#2d2d2d;
  --footer-bar:#1d1d1d;
  --white:#fff;
}
*{box-sizing:border-box;margin:0;padding:0}
html,body{width:763px;height:1200px;overflow:hidden}
body{font-family:"Open Sans",Arial,sans-serif;color:var(--ink);background:var(--white);position:relative}
a{color:inherit;text-decoration:none}

.site-header{height:56px;position:relative;border-bottom:1px solid var(--line)}
.brand{position:absolute;left:30px;top:12px;display:flex;align-items:center;gap:6px;font-family:"Roboto Slab",Georgia,serif;font-weight:700;font-size:18px;color:var(--red);line-height:1}
.brand-mark{width:11px;height:11px;background:var(--red);border-radius:50%}
.topbar{position:absolute;right:30px;top:4px;font-size:6.5px;color:var(--muted);display:flex;gap:14px}
.main-nav{position:absolute;right:30px;top:18px;display:flex;height:38px;font-size:8px;font-weight:600}
.main-nav a{padding:0 10px;display:flex;align-items:center;color:#444}
.main-nav a.active{background:var(--red);color:var(--white)}

.hero{position:absolute;top:56px;left:0;width:763px;height:267px;background:linear-gradient(180deg,#8a9aa8 0%,#b9b4aa 45%,#8e7a66 70%,#566049 100%)}
.hero-copy{position:absolute;left:95px;top:140px;color:var(--white)}
.hero-copy h1{font-size:17px;font-weight:600;margin-bottom:4px}
.hero-copy p{font-size:7.5px;max-width:230px;line-height:1.4;margin-bottom:12px}
.btn{display:inline-block;background:var(--red);color:var(--white);font-size:7px;font-weight:600;padding:6px 16px}
.hero-dots{position:absolute;right:10px;top:118px;display:flex;flex-direction:column;gap:5px}
.hero-dots span{width:6px;height:6px;border-radius:50%;background:rgba(255,255,255,.6)}
.hero-dots span.on{background:var(--white)}

.services{position:absolute;top:323px;left:0;width:763px;height:198px;background:linear-gradient(180deg,var(--navy) 0%,var(--navy-dark) 100%);color:var(--white);text-align:center}
.section-title{font-size:15px;font-weight:400;padding-top:22px}
.rule{width:50px;height:2px;background:var(--red);margin:6px auto 0}
.service-list{display:flex;justify-content:center;gap:34px;margin-top:20px;text-align:left}
.service{width:190px;display:flex;gap:8px}
.service svg{flex:none}
.service h3{font-size:9px;font-weight:600;margin-bottom:4px}
.service p{font-size:6.5px;line-height:1.5;color:#cfcde0}

.about{position:absolute;top:521px;left:0;width:763px;height:104px;text-align:center}
.about .section-title{color:#333;padding-top:8px}
.about p{font-size:6.5px;line-height:1.55;color:var(--muted);width:680px;margin:6px auto 6px}

.featured{position:absolute;top:625px;left:0;width:763px;height:196px}
.featured h2{font-size:14px;font-weight:600;color:var(--red);margin-left:40px;line-height:19px}
.products{display:flex;gap:14px;margin:10px 0 0 80px}
.product{width:140px;border:1px solid var(--line)}
.product-img{height:118px;background:linear-gradient(160deg,#f4f4f4,#c9c9c9)}
.product p{font-size:6.5px;text-align:center;padding:6px 4px;color:#555;border-top:1px solid var(--line)}
.arrow{position:absolute;top:88px;width:14px;height:22px;background:#ddd;display:flex;align-items:center;justify-content:center}
.arrow.prev{left:56px}.arrow.next{right:56px}

.brands{position:absolute;top:821px;left:0;width:763px;height:124px;text-align:center}
.brands .section-title{color:var(--navy);padding-top:20px}
.brand-row{display:flex;justify-content:center;align-items:center;gap:34px;margin-top:24px}
.brand-row span{font-size:13px;font-weight:700;color:var(--navy)}

.site-footer{position:absolute;top:945px;left:0;width:763px;height:225px;background:var(--footer);color:#bbb;display:flex;gap:40px;padding:70px 40px 0}
.site-footer h4{font-size:8px;color:var(--white);font-weight:600;margin-bottom:8px}
.site-footer p,.site-footer li{font-size:6.5px;line-height:1.7}
.site-footer ul{list-style:none}
.f-about{width:140px}.f-links{width:120px}.f-contact{width:170px}.f-form{width:170px}
.contact-row{display:flex;gap:6px;align-items:center;margin-bottom:6px}
.field{height:14px;background:#444;margin-bottom:5px;font-size:6px;padding:3px 5px;color:#999}
.field.tall{height:34px}
.send{float:right;background:var(--red);color:var(--white);font-size:6.5px;padding:4px 14px}
.footer-bar{position:absolute;top:1170px;left:0;width:763px;height:30px;background:var(--footer-bar);color:#888;font-size:6px;text-align:center;line-height:30px}
</style>
</head>
<body>
<header class="site-header">
  <a class="brand" href="#"><span class="brand-mark"></span>Harlow Packaging</a>
  <div class="topbar"><span>Email: info@harlowpack.com</span><span>Tel: +1 (555) 014-2276</span></div>
  <nav class="main-nav">
    <a class="active" href="#">Home</a>
    <a href="#">Packaging Products</a>
    <a href="#">Packaging Equipment Specials</a>
    <a href="#">Support</a>
    <a href="#">Contact Us</a>
  </nav>
</header>

<section class="hero" role="img" aria-label="Photo of the company headquarters building under a grey sky">
  <div class="hero-copy">
    <h1>Harlow Packaging</h1>
    <p>We design and build packaging systems that keep your line running every shift.</p>
    <a class="btn" href="#">Read More</a>
  </div>
  <div class="hero-dots"><span class="on"></span><span></span><span></span></div>
</section>

<section class="services">
  <h2 class="section-title">Our Services</h2>
  <div class="rule"></div>
  <div class="service-list">
    <div class="service">
      <svg width="16" height="16" viewBox="0 0 16 16"><circle cx="8" cy="8" r="7" fill="none" stroke="#fff"/><path d="M4.5 8.2l2.3 2.3 4.7-4.8" fill="none" stroke="#fff" stroke-width="1.4"/></svg>
      <div><h3>System Software</h3><p>Reliable controls and software support to keep your packaging line running at full speed every day.</p></div>
    </div>
    <div class="service">
      <svg width="16" height="16" viewBox="0 0 16 16"><circle cx="8" cy="8" r="7" fill="none" stroke="#fff"/><path d="M4.5 8.2l2.3 2.3 4.7-4.8" fill="none" stroke="#fff" stroke-width="1.4"/></svg>
      <div><h3>Field Service</h3><p>Trained technicians on site for installation, repairs and preventive care of shrink and seal systems.</p></div>
    </div>
    <div class="service">
      <svg width="16" height="16" viewBox="0 0 16 16"><circle cx="8" cy="8" r="7" fill="none" stroke="#fff"/><path d="M4.5 8.2l2.3 2.3 4.7-4.8" fill="none" stroke="#fff" stroke-width="1.4"/></svg>
      <div><h3>Parts Supply</h3><p>Fast shipping of genuine spare parts and consumables so downtime stays short and costs stay low.</p></div>
    </div>
  </div>
</section>

<section class="about">
  <h2 class="section-title">About Us</h2>
  <div class="rule"></div>
  <p>Harlow Packaging was founded by a small team of engineers who wanted to make packaging simpler for manufacturers of every size. Today we supply shrink wrappers, heat sealers, case sealers and carton erectors to customers across the region. Our staff helps you choose the right equipment, installs it on your floor and supports it for years. We also carry a wide range of films, tapes and spare parts, and our service team is ready whenever your line needs attention.</p>
  <a class="btn" href="#">Read More</a>
</section>

<section class="featured">
  <h2>Featured Products</h2>
  <div class="products">
    <div class="product"><div class="product-img" role="img" aria-label="Photo of a tunnel shrink wrapper"></div><p>TW-800 Tunnel Shrink Wrapper</p></div>
    <div class="product"><div class="product-img" role="img" aria-label="Photo of an L-bar shrink sealer"></div><p>LB-200 L-Bar Shrink Sealer</p></div>
    <div class="product"><div class="product-img" role="img" aria-label="Photo of a case sealer"></div><p>CS-100 Case Sealer</p></div>
    <div class="product"><div class="product-img" role="img" aria-label="Photo of a carton erector"></div><p>Carton Erector CE-50</p></div>
  </div>
  <span class="arrow prev"><svg width="6" height="8" viewBox="0 0 6 8"><path d="M5 0L1 4l4 4" fill="none" stroke="#666"/></svg></span>
  <span class="arrow next"><svg width="6" height="8" viewBox="0 0 6 8"><path d="M1 0l4 4-4 4" fill="none" stroke="#666"/></svg></span>
</section>

<section class="brands">
  <h2 class="section-title">Our Brands</h2>
  <div class="rule"></div>
  <div class="brand-row">
    <span>Tenvara</span><span>Boltline</span><span>Carrowell</span><span>Ridgeway</span><span>Quadra</span><span>Vexo</span>
  </div>
</section>

<footer class="site-footer">
  <div class="f-about"><h4>About</h4><p>Harlow Packaging supplies and services packaging equipment for manufacturers, with friendly support and quick parts delivery for every line we install.</p></div>
  <div class="f-links"><h4>Links</h4><ul><li>Product Files</li><li>Services</li><li>Terms &amp; Conditions</li><li>Site Map</li><li>Affiliates &amp; Vendors</li><li>Contact Us</li></ul></div>
  <div class="f-contact"><h4>Contact</h4>
    <div class="contact-row"><svg width="8" height="8" viewBox="0 0 8 8"><rect x=".5" y="1.5" width="7" height="5" fill="none" stroke="#bbb"/><path d="M.5 1.5l3.5 3 3.5-3" fill="none" stroke="#bbb"/></svg><p>info@harlowpack.com</p></div>
    <div class="contact-row"><svg width="8" height="8" viewBox="0 0 8 8"><path d="M1.5 1c1 0 1.5 1.5 1.5 2L2.3 4c.5 1 1 1.4 1.7 1.7L5 5c.5 0 2 .5 2 1.5L6 7.5C3.5 7.5.5 4.5.5 2z" fill="#bbb"/></svg><p>+1 (555) 014-2276</p></div>
    <div class="contact-row"><svg width="8" height="8" viewBox="0 0 8 8"><path d="M4 .5a2.5 2.5 0 0 1 2.5 2.5C6.5 5 4 7.5 4 7.5S1.5 5 1.5 3A2.5 2.5 0 0 1 4 .5z" fill="#bbb"/></svg><p>120 Mill Road, Springfield</p></div>
  </div>
  <div class="f-form"><h4>Contact Us</h4><div class="field">Name</div><div class="field">Email</div><div class="field tall">Message</div><span class="send">Send</span></div>
</footer>
<div class="footer-bar">Copyright © 2024 Harlow Packaging. All Rights Reserved.</div>
</body>
</html>
```